BUILDERS MERCHANTS BUSINESS CARD

we need a business card for our long established builders merchants
we supply to both trade and diy
we offer an express delivery service
we would like TWR to standout as this our main trade mark logo
also our main colours are blue/white/yellow

Industry/Entity Type

Trade

Contact Information for Business Card

TWR BUILDERS MERCHANTS

SUPPLIERS OF ALL TYPES OF BUILDING MATERIALS

-SAND/CEMENT
-BRICKS/BLOCKS
-PLASTER/PLASTERBOARDS
-INSULATION
-FENCING/GARDEN PAVING
-PLUMBING
-ELECTRICAL
-EXPRESS DELIVERIES

EST OVER 30 YEARS

418 MARSDEN VALE
LONDON
NORWOOD
SE19 4LT

0208 5492866
0208 3940587
FAX 0208359 2671
EMAIL- TWRBUILDERSMERCHANTS@QUILLMAIL.CO.UK

```html
<!DOCTYPE html>
<html lang="en">
<head>
<meta charset="utf-8">
<title>TWR Builders Merchants – Business Card</title>
<link rel="stylesheet" href="https://fonts.googleapis.com/css2?family=Questrial&family=Open+Sans:wght@700&display=swap">
<style>
  :root {
    --navy: #14275a;
    --yellow: #f2d21a;
    --white: #ffffff;
    --ink: #1d1d1d;
    --backdrop: #2b2b2b;
  }
  * { margin: 0; padding: 0; box-sizing: border-box; }
  html, body { width: 1200px; height: 900px; overflow: hidden; }
  body {
    background: var(--backdrop);
    display: flex; align-items: center; justify-content: center;
    font-family: "Questrial", "Century Gothic", sans-serif;
  }
  .card {
    position: relative;
    width: 980px; height: 560px;
    background: var(--white);
    overflow: hidden;
  }
  .brand {
    position: absolute; left: 64px; top: 78px;
    color: var(--navy);
    font-family: "Questrial", sans-serif;
    font-size: 66px; line-height: 0.9; letter-spacing: 1px;
    text-transform: uppercase;
  }
  .brand span { display: block; }
  .est-tag {
    position: absolute; left: 290px; top: 66px;
    background: var(--yellow); color: var(--navy);
    font-family: "Open Sans", sans-serif; font-weight: 700;
    font-size: 17px; padding: 3px 9px; letter-spacing: .5px;
  }
  .services {
    position: absolute; right: 48px; top: 86px;
    list-style: none; text-align: right;
    color: var(--ink); font-size: 22px; line-height: 1.5;
    text-transform: uppercase;
  }
  .contact-tab {
    position: absolute; left: 0; top: 296px;
    width: 62px; height: 230px;
    background: var(--navy);
    border-radius: 0 14px 14px 0;
    display: flex; flex-direction: column; align-items: center;
    justify-content: space-around; padding: 12px 0;
  }
  .contact-tab svg { width: 28px; height: 28px; fill: var(--white); }
  .contact-list {
    position: absolute; left: 100px; top: 300px;
    list-style: none; color: var(--ink);
    font-size: 22px; line-height: 44px;
  }
  .edge { position: absolute; left: 0; top: 0; }
</style>
</head>
<body>
  <main class="card">
    <div class="brand" aria-label="TWR Builders Merchants">
      <span>TWR</span><span>Builders</span><span>Merchants</span>
    </div>
    <div class="est-tag">EST OVER 30 YEARS</div>

    <ul class="services">
      <li>-Insulation</li>
      <li>-Sand/Cement</li>
      <li>-Bricks/Blocks</li>
      <li>-Plumbing/Electrical</li>
      <li>-Plaster/Plasterboards</li>
      <li>-Fencing/Garden Paving</li>
      <li>-Express Deliveries</li>
    </ul>

    <div class="contact-tab">
      <svg viewBox="0 0 24 24" aria-label="Phone"><path d="M3 9c0-3 4-5 9-5s9 2 9 5v2h-5V9c-1-1-7-1-8 0v2H3zM6 12h12l2 8H4zM10 14h4v4h-4z"/></svg>
      <svg viewBox="0 0 24 24" aria-label="Phone"><path d="M3 9c0-3 4-5 9-5s9 2 9 5v2h-5V9c-1-1-7-1-8 0v2H3zM6 12h12l2 8H4zM10 14h4v4h-4z"/></svg>
      <svg viewBox="0 0 24 24" aria-label="Fax"><path d="M7 3h10v6H7zM3 10h18v9H3zM6 13h8v2H6zM16 13h2v2h-2z"/></svg>
      <svg viewBox="0 0 24 24" aria-label="Email"><path d="M2 5h20v14H2zM4 7v1l8 5 8-5V7l-8 5z"/></svg>
      <svg viewBox="0 0 24 24" aria-label="Address"><path d="M12 2a7 7 0 0 0-7 7c0 5 7 13 7 13s7-8 7-13a7 7 0 0 0-7-7zm0 4a3 3 0 1 1 0 6 3 3 0 0 1 0-6z"/></svg>
    </div>

    <ul class="contact-list">
      <li>0208 549 2866</li>
      <li>0208 394 0587</li>
      <li>0208359 2671</li>
      <li>twrbuildersmerchants@quillmail.co.uk</li>
      <li>418 Marsden Vale, Norwood, London SE19 4LT</li>
    </ul>

    <svg class="edge" width="980" height="560" viewBox="0 0 980 560" aria-hidden="true">
      <path d="M0 542 H600 Q636 542 656 520 H980 V560 H0 Z" fill="var(--navy)"/>
      <path d="M648 528 Q670 502 716 502 H980 V520 H660 Z" fill="var(--yellow)"/>
    </svg>
  </main>
</body>
</html>
```